Book cover entitled #GLOWBEYONDIT

Design front book cover (self-self-portait photos included) for my first book entitled -

#GLOWBEYONDIT (may be best to have different shades of colour for glow beyond it to stand off you). I'm intentionally choosing a title that is essentially a hashtag.

Subtitle - Rewriting quiet inner battles

Concept of cover - left side of my face is shaded with shame and right side is brighter and hopeful. I have also include my logo.

Link for photos
https://www.filqorvex.com/sh/tq7mxd2kw9pl41a/BBR8NpXwQ3hLm6TzvKe2YUJ5b?dl=0

Target Market(s)

People (or friends & family) suffering with the shame of mental health struggles

Industry/Entity Type

Mental Health

Font styles to use
Other font styles liked:
• Avenir

Colors
3276b5
85acd3
cfdeed

Requirements
Must have
• Relatable, contemporary, authentic & compelling
• Link for photos
• https://www.filqorvex.com/sh/tq7mxd2kw9pl41a/BBR8NpXwQ3hLm6TzvKe2YUJ5b?dl=0
Nice to have
• Abstract & creative
Should not have
• Cheesy, plastic, pedestrian etc

```html
<!DOCTYPE html>
<html lang="en">
<head>
<meta charset="utf-8">
<title>#GLOWBEYONDIT — Book Cover</title>
<link rel="stylesheet" href="https://fonts.googleapis.com/css2?family=Antonio:wght@100;700&family=Nunito+Sans:wght@400;600&display=swap">
<style>
  :root {
    --stage: #232323;
    --cover-paper: #dfe6e8;
    --ink: #141414;
    --glow-orange: #ff6a13;
    --deep-navy: #1b1e3c;
    --mark-blue: #4a7ff0;
    --mark-grey: #7f858c;
  }
  * { margin: 0; padding: 0; box-sizing: border-box; }
  html, body {
    width: 1200px;
    height: 801px;
    overflow: hidden;
    background: var(--stage);
  }
  .book-cover {
    position: absolute;
    left: 351px;
    top: 28px;
    width: 498px;
    height: 745px;
    background: var(--cover-paper);
    overflow: hidden;
  }
  .author-mark {
    position: absolute;
    left: 24px;
    top: 30px;
    display: flex;
    align-items: center;
    gap: 7px;
  }
  .author-mark__square {
    width: 14px;
    height: 14px;
    background: var(--mark-blue);
  }
  .author-mark__name {
    font-family: "Nunito Sans", sans-serif;
    font-weight: 600;
    font-size: 15px;
    color: var(--mark-grey);
    letter-spacing: 0.02em;
  }
  .title {
    position: absolute;
    right: 40px;
    top: 22px;
    text-align: right;
    font-family: "Antonio", sans-serif;
    line-height: 0.98;
  }
  .title__hash {
    display: block;
    font-weight: 100;
    font-size: 116px;
    color: var(--ink);
    letter-spacing: 0.01em;
  }
  .title__accent {
    display: block;
    font-weight: 700;
    font-size: 104px;
    color: var(--glow-orange);
    letter-spacing: -0.01em;
  }
  .subtitle {
    position: absolute;
    right: 42px;
    top: 274px;
    text-align: right;
    font-family: "Nunito Sans", sans-serif;
    font-weight: 600;
    font-size: 15.5px;
    line-height: 1.32;
    letter-spacing: 0.12em;
    color: var(--ink);
    text-transform: uppercase;
  }
  .portrait-art {
    position: absolute;
    left: 38px;
    top: 330px;
    width: 440px;
    height: 415px;
    background:
      radial-gradient(ellipse at 55% 75%, var(--glow-orange) 0%, rgba(255,106,19,0.85) 35%, rgba(27,30,60,0) 70%),
      linear-gradient(160deg, var(--deep-navy) 0%, #2a2b4a 45%, var(--glow-orange) 100%);
    border-radius: 180px 180px 0 0;
  }
</style>
</head>
<body>
  <main class="book-cover">
    <div class="author-mark">
      <span class="author-mark__square"></span>
      <span class="author-mark__name">ned calder</span>
    </div>

    <h1 class="title">
      <span class="title__hash">#GLOW</span>
      <span class="title__accent">BEYOND IT</span>
    </h1>

    <p class="subtitle">Rewriting<br>quiet inner<br>battles</p>

    <div class="portrait-art" role="img" aria-label="Illustrated profile of a man with bowed head, a tangle of scribbled lines in his mind and shards breaking off his shoulder, in navy and orange"></div>
  </main>
</body>
</html>
```